Christmas CD Cover and on body disc design

2 page Welsh language Christmas CD cover, front and back plus disc design. Easy listening pop album, ballads with a few upbeat tunes thrown in. Ima...

Industry/Entity Type

Music Download

Requirements
Must have
• Christmas feel. Traditional but not old fashioned.
Nice to have
• Warm feeling

```html
<!DOCTYPE html>
<html lang="cy">
<head>
<meta charset="utf-8">
<title>Yr Albwm Nadolig – Disc</title>
<link rel="stylesheet" href="https://fonts.googleapis.com/css2?family=Cinzel:wght@900&family=Dancing+Script:wght@700&family=Courier+Prime&display=swap">
<style>
  :root {
    --page: #ffffff;
    --disc-red: #a8182a;
    --disc-deep: #8c1020;
    --glow-orange: #e7892f;
    --glow-amber: #d4602a;
    --gold-light: #f0d48a;
    --gold: #c99a3c;
    --gold-dark: #8a5a1a;
    --hub-ring: #c9a27a;
    --hub-lilac: #8f8aa8;
    --hub-hole: #ffffff;
    --name-teal: #1f8c8c;
    --name-outline: #ffffff;
    --small-ink: #f4e6c8;
    --label-black: #111111;
  }
  html, body {
    margin: 0;
    padding: 0;
    width: 1200px;
    height: 1185px;
    overflow: hidden;
    background: var(--page);
  }
  .disc-canvas {
    display: block;
    width: 1200px;
    height: 1185px;
  }
  .album-title {
    font-family: "Cinzel", "Georgia", serif;
    font-weight: 900;
    font-size: 104px;
    fill: url(#goldFoil);
    stroke: var(--gold-dark);
    stroke-width: 1.5;
  }
  .artist-name {
    font-family: "Dancing Script", "Brush Script MT", cursive;
    font-weight: 700;
    fill: var(--name-teal);
    stroke: var(--name-outline);
    stroke-width: 4;
    paint-order: stroke fill;
  }
  .artist-name--left { font-size: 78px; }
  .artist-name--right { font-size: 104px; }
  .catalogue-line {
    font-family: "Courier Prime", "Courier New", monospace;
    font-size: 16px;
    fill: var(--small-ink);
    text-anchor: middle;
  }
  .label-name {
    font-family: "Courier Prime", "Courier New", monospace;
    font-size: 11px;
    fill: var(--page);
    text-anchor: middle;
    letter-spacing: 0.5px;
  }
</style>
</head>
<body>
<svg class="disc-canvas" viewBox="0 0 1200 1185" xmlns="http://www.w3.org/2000/svg">
  <defs>
    <clipPath id="discShape">
      <circle cx="600" cy="592" r="585"/>
    </clipPath>
    <radialGradient id="discGlow" cx="50%" cy="58%" r="55%">
      <stop offset="0%" stop-color="var(--glow-orange)"/>
      <stop offset="45%" stop-color="var(--glow-amber)"/>
      <stop offset="85%" stop-color="var(--disc-red)"/>
      <stop offset="100%" stop-color="var(--disc-deep)"/>
    </radialGradient>
    <linearGradient id="goldFoil" x1="0" y1="0" x2="0" y2="1">
      <stop offset="0%" stop-color="var(--gold-light)"/>
      <stop offset="55%" stop-color="var(--gold)"/>
      <stop offset="100%" stop-color="var(--gold-dark)"/>
    </linearGradient>
    <linearGradient id="leftPortraitTone" x1="0" y1="0" x2="1" y2="1">
      <stop offset="0%" stop-color="#3a2a2e"/>
      <stop offset="45%" stop-color="#d9a890"/>
      <stop offset="100%" stop-color="#e8c0a8"/>
    </linearGradient>
    <linearGradient id="rightPortraitTone" x1="0" y1="0" x2="1" y2="1">
      <stop offset="0%" stop-color="#d89a6e"/>
      <stop offset="50%" stop-color="#b98a74"/>
      <stop offset="100%" stop-color="#4a4a52"/>
    </linearGradient>
    <radialGradient id="softFade" cx="50%" cy="50%" r="50%">
      <stop offset="55%" stop-color="#fff" stop-opacity="1"/>
      <stop offset="100%" stop-color="#fff" stop-opacity="0"/>
    </radialGradient>
    <mask id="leftFade">
      <rect x="40" y="380" width="420" height="660" fill="url(#softFade)"/>
    </mask>
    <mask id="rightFade">
      <rect x="680" y="340" width="500" height="680" fill="url(#softFade)"/>
    </mask>
  </defs>

  <g class="disc" clip-path="url(#discShape)">
    <circle class="disc-base" cx="600" cy="592" r="585" fill="url(#discGlow)"/>

    <rect class="portrait portrait--left" x="40" y="380" width="420" height="660"
          fill="url(#leftPortraitTone)" mask="url(#leftFade)"
          role="img" aria-label="Portrait photograph of the female singer"/>
    <rect class="portrait portrait--right" x="680" y="340" width="500" height="680"
          fill="url(#rightPortraitTone)" mask="url(#rightFade)"
          role="img" aria-label="Portrait photograph of the male singer"/>

    <g class="album-title-group">
      <text class="album-title" x="270" y="200" textLength="660" lengthAdjust="spacing">YR ALBWM</text>
      <text class="album-title" x="292" y="372" textLength="608" lengthAdjust="spacing">NADOLIG</text>
    </g>

    <g class="disc-hub">
      <circle cx="590" cy="578" r="136" fill="var(--hub-ring)"/>
      <circle cx="590" cy="578" r="130" fill="var(--hub-lilac)"/>
      <circle cx="590" cy="578" r="78" fill="var(--hub-hole)"/>
    </g>

    <g class="artist-names">
      <text class="artist-name artist-name--left" x="285" y="835" text-anchor="middle">Mari</text>
      <text class="artist-name artist-name--left" x="325" y="940" text-anchor="middle">Ellis</text>
      <text class="artist-name artist-name--right" x="870" y="865" text-anchor="middle">Rhys</text>
      <text class="artist-name artist-name--right" x="925" y="970" text-anchor="middle">Morgan</text>
    </g>

    <g class="catalogue-info">
      <text class="catalogue-line" x="600" y="1052">RF024</text>
      <text class="catalogue-line" x="600" y="1084">©Rhys Morgan • Recordiau'r Ffrwd 2017</text>
    </g>

    <g class="record-label">
      <rect x="527" y="1106" width="146" height="90" fill="var(--label-black)"/>
      <text class="label-name" x="600" y="1172">RECORDIAU'R FFRWD</text>
    </g>
  </g>
</svg>
</body>
</html>
```